Crestline Slate & Tile Needs a Business Card

Attached you will find your logo, my photo and design guidelines for a new business card. The final design will need two separate files to create an embossed card. The cards will be printed by www.plinkprint.com (Instructions below)
Format is the Zib SQUARE card
Crestline Slate And Tile is a brick and mortar, retail stone and tile shop.
One the front:
Crestline Slate And Tile
Gerald Finchcombe
Owner
48207 Vesper Hollow Blvd
Suite R & T
Charlotte, NC 28953
Cell: 704-555-0183
Web: www.CrestlineSlateAndTile.com
(Make each word of the domain a different or alternating color)
On the back;
Something that shows beautiful colorful tile
Follow the design guide closely please. For more information see this page that describes creating the spot gloss file: https://www.plinkprint.com/us/business-cards/design-guidelines-spot-gloss
The logo is what we would like to have raised spot glossed.
Format is the Zib SQUARE card. See attahced guidlines.

```html
<!DOCTYPE html>
<html lang="en">
<head>
<meta charset="utf-8">
<title>Crestline Slate &amp; Tile — Business Card</title>
<link rel="stylesheet" href="https://fonts.googleapis.com/css2?family=Lexend:wght@400;600&display=swap">
<style>
  :root {
    --page-bg: #e6e6e6;
    --card-bg: #ffffff;
    --rust: #a13d1f;
    --navy: #1f3440;
    --ink: #1c1c1c;
    --gold: #b07a3a;
    --slate: #4f6170;
  }
  * { box-sizing: border-box; margin: 0; padding: 0; }
  html, body {
    width: 1200px; height: 1200px; overflow: hidden;
    background: var(--page-bg);
    font-family: "Lexend", "Helvetica Neue", Arial, sans-serif;
  }
  .card {
    position: absolute; left: 204px; width: 792px; height: 529px;
    background: var(--card-bg);
  }
  .card--front { top: 50px; }
  .card--back { top: 621px; }

  /* Front: brand mark area */
  .brand-block {
    position: absolute; left: 60px; top: 100px; width: 315px;
    display: flex; flex-direction: column; align-items: center; gap: 22px;
  }
  .brand-square { width: 120px; height: 120px; background: var(--navy); }
  .brand-name {
    font-weight: 600; font-size: 26px; color: var(--navy);
    text-align: center; line-height: 1.3;
  }

  /* Front: contact details */
  .person { position: absolute; right: 57px; top: 78px; text-align: right; }
  .person__name { font-weight: 600; font-size: 32px; color: var(--rust); line-height: 1; }
  .person__role { font-weight: 400; font-size: 20px; color: var(--ink); margin-top: 14px; line-height: 1; }

  .divider {
    position: absolute; left: 475px; top: 205px; width: 260px; height: 10px;
  }
  .divider::before {
    content: ""; position: absolute; left: 0; right: 0; top: 4px;
    border-top: 1.5px solid var(--gold);
  }
  .divider__diamond {
    position: absolute; left: 126px; top: 1px; width: 8px; height: 8px;
    background: var(--gold); transform: rotate(45deg);
    outline: 3px solid var(--card-bg);
  }

  .contact {
    position: absolute; right: 30px; top: 255px;
    font-size: 21px; color: var(--ink); line-height: 27px; text-align: right;
  }
  .contact__row { display: flex; justify-content: flex-end; align-items: flex-start; gap: 12px; }
  .contact__row + .contact__row { margin-top: 6px; }
  .contact__row--web { margin-top: 38px !important; }
  .contact__icon { width: 17px; height: 17px; flex: none; margin-top: 5px; }
  .contact__lines { display: flex; flex-direction: column; }

  /* Back: brand lockup */
  .lockup {
    position: absolute; left: 118px; top: 192px; height: 145px;
    display: flex; align-items: center; gap: 48px;
  }
  .lockup__square { width: 118px; height: 118px; background: var(--navy); }
  .lockup__name { font-weight: 600; font-size: 42px; color: var(--navy); line-height: 1; }
</style>
</head>
<body>

<section class="card card--front" aria-label="Business card front">
  <div class="brand-block">
    <div class="brand-square"></div>
    <p class="brand-name">Crestline Slate &amp; Tile</p>
  </div>

  <div class="person">
    <h1 class="person__name">Gerald Finchcombe</h1>
    <p class="person__role">Owner</p>
  </div>

  <div class="divider"><span class="divider__diamond"></span></div>

  <div class="contact">
    <div class="contact__row">
      <span>704-555-0183</span>
      <svg class="contact__icon" viewBox="0 0 24 24" aria-hidden="true">
        <path d="M6.6 2.5l3 3.2-1.9 2.6c1.3 2.9 3.5 5.1 6.4 6.5l2.6-1.9 3.2 3-1.6 3.4c-7.6-.4-13.6-6.5-14-14z" fill="none" stroke="var(--rust)" stroke-width="2" stroke-linejoin="round"/>
        <path d="M14 3.5a7 7 0 0 1 6.5 6.5M14 7a3.5 3.5 0 0 1 3 3" fill="none" stroke="var(--rust)" stroke-width="1.8" stroke-linecap="round"/>
      </svg>
    </div>
    <div class="contact__row">
      <span class="contact__lines">
        <span>48207 Vesper Hollow Blvd</span>
        <span>Suite R &amp; T</span>
        <span>Charlotte, NC 28953</span>
      </span>
      <svg class="contact__icon" viewBox="0 0 24 24" aria-hidden="true">
        <path d="M12 23s-7.5-8.3-7.5-13.5a7.5 7.5 0 0 1 15 0C19.5 14.7 12 23 12 23z" fill="var(--rust)"/>
        <circle cx="12" cy="9.5" r="2.8" fill="var(--card-bg)"/>
      </svg>
    </div>
    <div class="contact__row contact__row--web">
      <span>www.CrestlineSlateAndTile.com</span>
      <svg class="contact__icon" viewBox="0 0 24 24" aria-hidden="true">
        <g fill="none" stroke="var(--rust)" stroke-width="1.6">
          <circle cx="12" cy="12" r="10"/>
          <ellipse cx="12" cy="12" rx="4.5" ry="10"/>
          <path d="M2 12h20M4 6.5h16M4 17.5h16"/>
        </g>
      </svg>
    </div>
  </div>
</section>

<section class="card card--back" aria-label="Business card back">
  <div class="lockup">
    <div class="lockup__square"></div>
    <p class="lockup__name">Crestline Slate &amp; Tile</p>
  </div>
</section>

</body>
</html>
```